redesing professional certificate

Redesign our certificate to more a professional look and to make it look like a-wanna have - Best in adobe photoshop, because this template will be our basic, and we have in our education different levels, basic, upper, lower, complex, master level. I usually add a small picture to show what level they are. Or when you have a better suggestion I a gladly to hear.
We teach to physiotherapist so it has to look professional.

Target Market(s)

physiotherapist

Industry/Entity Type

Health Care

Requirements
Must have
• our logo

```html
<!DOCTYPE html>
<html lang="en">
<head>
<meta charset="utf-8">
<title>Certificate – Myofascial Balance Method</title>
<link rel="stylesheet" href="https://fonts.googleapis.com/css2?family=Days+One&family=Montserrat+Alternates:ital,wght@1,400&family=Arimo&display=swap">
<style>
  :root {
    --navy: #14294a;
    --gold: #f7c52a;
    --sky-deep: #1f6fbd;
    --sky-light: #a9d4f2;
    --mist: #dcebf7;
    --paper: #ffffff;
  }
  * { margin: 0; padding: 0; box-sizing: border-box; }
  html, body { width: 922px; height: 1200px; overflow: hidden; }
  body { position: relative; background: var(--paper); color: var(--navy); }

  .backdrop {
    position: absolute; inset: 0;
    background: linear-gradient(120deg, #c4ddf2 0%, var(--mist) 60%, #eef5fb 100%);
  }
  .side-pattern {
    position: absolute; left: 0; top: 0; width: 290px; height: 1200px;
    background: linear-gradient(90deg, var(--sky-deep) 0%, #4f97d6 55%, var(--sky-light) 100%);
  }
  .card {
    position: absolute; left: 290px; top: 92px; width: 586px; height: 1060px;
    background: var(--paper);
    border: 5px solid var(--gold); border-left: none;
    border-radius: 0 34px 34px 0;
  }

  .brand-mark {
    position: absolute; left: 514px; top: 22px; width: 136px; height: 136px;
    border-radius: 50%; background: var(--navy); border: 3px solid var(--paper);
    display: flex; align-items: center; justify-content: center;
  }
  .brand-name {
    font-family: "Days One", sans-serif; font-size: 34px; color: var(--gold); letter-spacing: 1px;
  }

  .center { position: absolute; left: 290px; width: 584px; text-align: center; }

  .title {
    top: 158px; font-family: "Days One", sans-serif; font-size: 98px; line-height: 1; color: var(--navy);
  }
  .recipient {
    top: 298px; font-family: "Arimo", sans-serif; font-size: 42px; line-height: 1;
  }
  .rule { position: absolute; height: 2px; background: var(--gold); }
  .rule.name-rule { left: 310px; top: 362px; width: 538px; }

  .italic { font-family: "Montserrat Alternates", sans-serif; font-style: italic; font-weight: 400; }
  .statement { top: 368px; font-size: 26px; line-height: 30px; }

  .signatory { position: absolute; width: 216px; text-align: center; }
  .signatory .rule { position: static; margin-bottom: 2px; }
  .signatory .name { font-size: 22px; line-height: 24px; }
  .signatory .role { font-size: 19px; line-height: 22px; }
  .signatory.left { left: 334px; top: 577px; }
  .signatory.right { left: 621px; top: 577px; }

  .registration { top: 632px; font-size: 19px; line-height: 24px; }
  .maintenance { top: 682px; font-size: 21px; line-height: 30px; }

  .seal { position: absolute; left: 530px; top: 832px; }

  .tagline { top: 1003px; font-size: 24px; line-height: 30px; }
  .address { top: 1052px; font-size: 18px; line-height: 21.5px; }
</style>
</head>
<body>
  <div class="backdrop" role="img" aria-label="Faint light-blue fascia network pattern"></div>
  <div class="side-pattern" role="img" aria-label="Blue panel with interwoven fascia fibre pattern"></div>

  <main class="card"></main>

  <div class="brand-mark"><span class="brand-name">MBM</span></div>

  <h1 class="center title">Certificate</h1>
  <p class="center recipient">Marco Delgado</p>
  <div class="rule name-rule"></div>

  <p class="center italic statement">
    has completed the fasciatherapy<br>
    level I course 3 days<br>
    15-17 february 2020<br>
    Kópavogur, Iceland 17 february 2020.
  </p>

  <div class="signatory left italic">
    <div class="rule"></div>
    <p class="name">Mr. JT Holman</p>
    <p class="role">Co-Director</p>
  </div>
  <div class="signatory right italic">
    <div class="rule"></div>
    <p class="name">Mr. BK Sarin</p>
    <p class="role">Co-Director</p>
  </div>

  <p class="center italic registration">Registration number: 7 ICE 20</p>

  <p class="center italic maintenance">
    The Myofascial Balance Method ongoing<br>
    certification is contingent upon<br>
    meeting the requirements of the<br>
    maintenance of the certification<br>
    of Fasciatherapy
  </p>

  <svg class="seal" width="104" height="162" viewBox="0 0 104 162" aria-hidden="true">
    <path d="M30 70 L4 152 L26 140 L36 162 L52 104 L68 162 L78 140 L100 152 L74 70 Z" fill="var(--navy)"/>
    <circle cx="52" cy="52" r="50" fill="var(--navy)"/>
    <circle cx="52" cy="52" r="38" fill="none" stroke="var(--paper)" stroke-width="2"/>
  </svg>

  <p class="center italic tagline">Specialists in fasciatherapy innovation</p>
  <p class="center italic address">
    Tissueline BV<br>
    Lindengracht 48<br>
    1015KK Amsterdam<br>
    The Netherlands
  </p>
</body>
</html>
```